Business Card for Brenwick Painting

We need a simple, yet out standing business card for our painting company.

Target Market(s)

wealthy; high-end neighborhoods, and businesses

Industry/Entity Type

Painting

Contact Information for Business Card

Name:
Dorian Vask

Email:
d.vask@brenwick-painting.example

Website:
Brenwick-painting.example

Phone Number:
(555) 412-9063

Font styles to use
Serif
Sans Serif

Requirements
Must have
• slogan "making change simple"
Should not have
• A title attached to the name on the card

```html
<!DOCTYPE html>
<html lang="en">
<head>
<meta charset="UTF-8">
<title>Brenwick Painting – Business Card</title>
<link href="https://fonts.googleapis.com/css2?family=Lora:ital,wght@0,400;0,500;1,400&display=swap" rel="stylesheet">
<style>
  :root {
    --bg: #a19d9d;
    --card: #fbfbfa;
    --green-dark: #41552f;
    --green-light: #8cc43f;
    --text: #4a5e37;
  }
  * { margin: 0; padding: 0; box-sizing: border-box; }
  html, body { width: 1200px; height: 1200px; overflow: hidden; }
  body {
    background: var(--bg);
    position: relative;
    font-family: "Lora", Georgia, serif;
    color: var(--text);
  }
  .card {
    position: absolute;
    width: 712px;
    height: 420px;
    background: var(--card);
    overflow: hidden;
  }
  .card--front { left: 238px; top: 118px; }
  .card--back { left: 230px; top: 644px; }

  .brand-art {
    position: absolute;
    background: linear-gradient(135deg, var(--green-light) 0%, #6e9a3a 50%, var(--green-dark) 100%);
    opacity: 0.9;
  }
  .card--front .brand-art {
    left: 0; top: 0; width: 320px; height: 420px;
    clip-path: polygon(0 0, 45% 0, 100% 100%, 0 100%);
  }
  .card--back .brand-art {
    right: 0; bottom: 0; width: 292px; height: 282px;
    clip-path: polygon(52% 0, 72% 0, 100% 40%, 100% 100%, 0 100%);
  }

  .wordmark {
    position: absolute;
    display: flex;
    align-items: center;
    gap: 14px;
  }
  .wordmark__square {
    width: 40px; height: 40px;
    background: var(--green-light);
    flex: none;
  }
  .wordmark__name {
    font-family: "Lora", Georgia, serif;
    font-weight: 500;
    font-size: 34px;
    line-height: 1;
    color: var(--green-dark);
    white-space: nowrap;
  }
  .card--front .wordmark { left: 314px; top: 188px; }
  .card--back .wordmark { left: 102px; top: 58px; }
  .card--back .wordmark__name { font-size: 30px; }

  .band-dark {
    position: absolute; left: 0; top: 0;
    width: 60px; height: 100%;
    background: var(--green-dark);
  }
  .band-light {
    position: absolute; left: 62px; top: 0;
    width: 6px; height: 100%;
    background: var(--green-light);
  }

  .person { position: absolute; left: 102px; top: 218px; }
  .person__name {
    font-size: 29px;
    font-weight: 400;
    color: var(--text);
    line-height: 1.1;
  }
  .slogan {
    font-size: 15px;
    font-style: italic;
    color: var(--text);
    margin-top: 2px;
  }

  .contact {
    position: absolute; left: 102px; top: 292px;
    list-style: none;
  }
  .contact__item {
    display: flex; align-items: center;
    height: 29px;
    font-size: 17px;
    color: var(--text);
    white-space: nowrap;
  }
  .contact__icon { width: 16px; height: 16px; margin-right: 22px; flex: none; }
</style>
</head>
<body>

  <section class="card card--front" aria-label="Business card front">
    <div class="brand-art" role="img" aria-label="Large decorative brand mark area in green tones"></div>
    <div class="wordmark">
      <span class="wordmark__square"></span>
      <span class="wordmark__name">Brenwick Painting</span>
    </div>
  </section>

  <section class="card card--back" aria-label="Business card back">
    <div class="band-dark"></div>
    <div class="band-light"></div>

    <div class="wordmark">
      <span class="wordmark__square"></span>
      <span class="wordmark__name">Brenwick Painting</span>
    </div>

    <div class="person">
      <h1 class="person__name">Dorian Vask</h1>
      <p class="slogan">making change simple</p>
    </div>

    <ul class="contact">
      <li class="contact__item">
        <svg class="contact__icon" viewBox="0 0 16 16" aria-hidden="true">
          <path d="M1 6 Q8 1 15 6 L13 8 L11 6 L5 6 L3 8 Z" fill="var(--text)"/>
          <rect x="3" y="8" width="10" height="6" rx="1" fill="var(--text)"/>
        </svg>
        (555) 412-9063
      </li>
      <li class="contact__item">
        <svg class="contact__icon" viewBox="0 0 16 16" aria-hidden="true">
          <rect x="1" y="3" width="14" height="10" fill="var(--text)"/>
          <path d="M1 3 L8 9 L15 3" stroke="var(--card)" stroke-width="1.3" fill="none"/>
        </svg>
        d.vask@brenwick-painting.example
      </li>
      <li class="contact__item">
        <svg class="contact__icon" viewBox="0 0 16 16" aria-hidden="true">
          <circle cx="8" cy="8" r="6.5" fill="none" stroke="var(--text)" stroke-width="1.4"/>
          <ellipse cx="8" cy="8" rx="3" ry="6.5" fill="none" stroke="var(--text)" stroke-width="1.1"/>
          <line x1="1.5" y1="8" x2="14.5" y2="8" stroke="var(--text)" stroke-width="1.1"/>
        </svg>
        www.Brenwick-painting.example
      </li>
    </ul>

    <div class="brand-art" role="img" aria-label="Large decorative brand mark area in green tones"></div>
  </section>

</body>
</html>
```